Anwaltskanzlei sucht Design für Geschäftspapier, Visitenkarten, Marketing unter Einbindung des neuen Logos
Zielgruppe
Anwaltliche Rechtsberatung und Rechtsvertretung auf den Gebieten des Arbeits-, Gesellschafts- und Wirtschaftsrechts sowie des Datenschutzrechts
Zielgruppe: Mittelständische Unternehmen aller Rechtsformen und Branchen
In Kooperation mit Kanzlei Velbrand (www.kanzlei-velbrand.de)
Inhaber einer weiteren Kanzlei Velbrand & Krüger
Aufgabenstellung
Einbindung des übersandten Logos
ggf. Slogan: Kanzlei für den Mittelstand
optional: Nennung der Rechtsgebiete

```html
<!DOCTYPE html>
<html lang="de">
<head>
<meta charset="utf-8">
<title>Anwaltskanzlei Hossmer – Briefbogen</title>
<link href="https://fonts.googleapis.com/css2?family=Montserrat:wght@300;400;500&family=Open+Sans:wght@400&display=swap" rel="stylesheet">
<style>
  :root {
    --navy: #1f2d4c;
    --steel: #b7b9bd;
    --text-grey: #8a8c90;
    --paper: #ffffff;
  }
  * { margin: 0; padding: 0; box-sizing: border-box; }
  html, body { width: 848px; height: 1200px; overflow: hidden; background: var(--paper); }
  .letterhead {
    position: relative; width: 848px; height: 1200px; overflow: hidden;
    font-family: "Montserrat", sans-serif; color: var(--text-grey);
  }
  .header-band { position: absolute; left: 0; top: 0; width: 848px; height: 78px; background: var(--steel); }
  .header-strip { position: absolute; left: 0; top: 78px; width: 848px; height: 42px; background: var(--navy); }
  .header-corner { position: absolute; left: 0; top: 0; width: 92px; height: 78px; background: var(--navy); }
  .firm-name {
    position: absolute; right: 107px; top: 27px;
    display: flex; align-items: center; gap: 7px;
    font-weight: 400; font-size: 10.5px; line-height: 11px; letter-spacing: 0.2px;
    color: var(--navy);
  }
  .firm-name .mark { width: 12px; height: 12px; background: var(--navy); flex: none; }
  .slogan {
    position: absolute; right: 108px; top: 92px;
    font-weight: 400; font-size: 11.5px; letter-spacing: 0.4px; color: #d6d8dc;
  }
  .recipient { position: absolute; left: 118px; top: 236px; color: var(--navy); }
  .recipient .to { font-size: 13px; font-weight: 400; }
  .recipient .name { font-size: 14px; font-weight: 400; margin-top: 5px; }
  .recipient address {
    font-style: normal; font-weight: 300; font-size: 11px; line-height: 17.2px;
    color: var(--text-grey); margin: 3px 0 0 8px;
  }
  .date { position: absolute; right: 108px; top: 238px; font-size: 10.5px; font-weight: 400; color: #5f6166; }
  .body-copy {
    position: absolute; left: 125px; top: 383px; width: 616px;
    font-weight: 300; font-size: 13.6px; line-height: 17.1px;
    text-align: justify; hyphens: auto; color: var(--text-grey);
  }
  .body-copy p + p { margin-top: 17.1px; }
  .signature {
    position: absolute; left: 517px; top: 909px; width: 200px; height: 92px;
    background: linear-gradient(90deg, rgba(31,45,76,0.10), rgba(31,45,76,0.18));
    border-radius: 4px;
  }
  .role { position: absolute; right: 108px; top: 974px; font-size: 16px; font-weight: 300; color: var(--text-grey); }
  .footer-line { position: absolute; left: 0; top: 1135px; width: 848px; height: 10px; background: var(--steel); }
  .footer-band { position: absolute; left: 0; top: 1145px; width: 848px; height: 55px; background: var(--navy); }
  .footer-badge {
    position: absolute; left: 51px; top: 1114px; width: 68px; height: 66px;
    background: var(--navy); border: 2px solid var(--paper); border-radius: 2px;
  }
  .contact {
    position: absolute; display: flex; align-items: center; gap: 10px;
    font-family: "Open Sans", sans-serif; font-size: 8px; line-height: 10.5px; color: var(--paper);
  }
  .contact svg { flex: none; }
  .contact.phone { left: 265px; top: 1159px; }
  .contact.person { left: 427px; top: 1158px; }
  .contact.place { left: 596px; top: 1152px; }
</style>
</head>
<body>
<main class="letterhead">
  <div class="header-band"></div>
  <div class="header-strip"></div>
  <div class="header-corner"></div>

  <div class="firm-name"><span class="mark"></span><span>ANWALTSKANZLEI<br>HOSSMER</span></div>
  <div class="slogan">KANZLEI FÜR DEN MITTELSTAND</div>

  <section class="recipient">
    <div class="to">TO</div>
    <div class="name">Name Surname</div>
    <address>Human Resources<br>123 Inc.<br>1105-D ABCD, EFG<br>Germany</address>
  </section>
  <div class="date">Friday, 01/03/2022</div>

  <article class="body-copy">
    <p>Lorem ipsum dolor sit amet, consectetur adipiscing elit. Pellentesque facilisis sollicitudin ante. Pellentesque habitant morbi tristique senectus et netus et malesuada fames ac turpis egestas. Nunc feugiat tortor nunc, quis feugiat lectus mattis sit amet. Nunc urna velit, convallis scelerisque odio non, pulvinar tincidunt massa. Proin pulvinar lacus at ex auctor consequat. Maecenas eleifend tempus posuere. Aliquam non pretium metus. Mauris nibh velit, molestie et lorem quis, hendrerit lacinia nunc. Donec in dignissim augue. Curabitur vitae erat nisi. Vestibulum ante ipsum primis in faucibus orci luctus et ultrices posuere cubilia Curae; Aliquam blandit magna ac augue placerat luctus. Ut et vehicula odio. Vivamus tincidunt diam diam, sed facilisis lectus pretium quis. Sed vel mi accumsan, luctus metus vel, congue ex.</p>
    <p>Curabitur non tristique tellus. Nam maximus fermentum metus sit amet luctus. Cras semper nunc id urna lacinia, in interdum quam mollis. Mauris sit amet eros vel lorem facilisis semper non ac nunc. Curabitur ornare suscipit lacus. Duis sit amet lectus vitae nulla consectetur ullamcorper vitae id urna. Sed dictum at lectus eget vehicula. Phasellus non lacinia nunc. Mauris ex tortor, ultricies luctus lectus egestas, gravida ornare elit. In tempor libero non ullamcorper sagittis. Phasellus interdum pulvinar lacus vel sodales. Praesent nec velit bibendum, accumsan magna non, molestie tortor. Nam a est at arcu porta auctor quis id tortor.</p>
    <p>Pellentesque habitant morbi tristique senectus et netus et malesuada fames ac turpis egestas. Nulla laoreet nec ex nec sagittis. Ut et vulputate magna. Nullam vehicula dapibus elit sagittis laoreet. Morbi dignissim ultricies libero at pulvinar. Sed leo tellus, ultricies nec erat sed, fermentum rhoncus odio. Pellentesque habitant morbi tristique senectus et netus et malesuada fames ac turpis egestas. Nullam egestas cursus dapibus. Nunc quis sodales nulla. Integer non ante tincidunt, facilisis mauris sed, rutrum neque. Curabi-</p>
  </article>

  <div class="signature" role="img" aria-label="Handschriftliche Unterschrift des Absenders"></div>
  <div class="role">Responsability</div>

  <div class="footer-line"></div>
  <div class="footer-band"></div>
  <div class="footer-badge"></div>

  <div class="contact phone">
    <svg width="18" height="18" viewBox="0 0 24 24" fill="none" stroke="#ffffff" stroke-width="1.4" stroke-linejoin="round">
      <path d="M5 3h4l2 5-2.5 1.5a11 11 0 0 0 6 6L16 13l5 2v4a2 2 0 0 1-2 2A16 16 0 0 1 3 5a2 2 0 0 1 2-2z"/>
      <path d="M15 3a6 6 0 0 1 6 6M15 6.5a2.5 2.5 0 0 1 2.5 2.5"/>
    </svg>
    <span>+49 (0) 12345678910</span>
  </div>
  <div class="contact person">
    <svg width="16" height="20" viewBox="0 0 16 20" fill="none" stroke="#ffffff" stroke-width="1.4">
      <circle cx="8" cy="5" r="4"/>
      <path d="M1 20v-2a7 7 0 0 1 14 0v2"/>
    </svg>
    <span>Name Surname<br>N.Surname@hossmer-recht.de</span>
  </div>
  <div class="contact place">
    <svg width="16" height="20" viewBox="0 0 16 20" fill="none" stroke="#ffffff" stroke-width="1.4">
      <path d="M8 19s-7-7-7-11a7 7 0 0 1 14 0c0 4-7 11-7 11z"/>
      <circle cx="8" cy="8" r="2.5"/>
    </svg>
    <span>123 Av.<br>4567 ABCD City<br>Germany</span>
  </div>
</main>
</body>
</html>
```